Face cream packaging | Cosmetic start-up

This project is about creating design proposals for two different types of packaging. Once to a cream jar made of glass and once to a jar made of plastic.
Three different designs must be created for each type of jar. Later, the different packaging will be used as customization options in an online store for cosmetics.

- The packaging variant made of glass should have color gradients. Three different shades are to be chosen. (Preferably with the primary colors red, blue and green). Note: The designer can create other proposals at will if he has better ideas. The logo must be included in some form. (Link to manufacturer description: https://catalogue.valdorpackaging.com/en/portals/valdorpackaging/assets/12667188/lou-50-ml/)

- With the plastic type of packaging, the designer has a lot of freedom to design. The only requirement is that the design must be artistic. It doesn't matter whether abstract patterns, geometric figures, mandalas or just a basic color is chosen. The main thing is that the packaging inspires. The logo must be included in some form. (Link to manufacturer description: https://catalogue.valdorpackaging.com/en/portals/valdorpackaging/assets/12667181/edda-50-ml/)

Thank you in advance for your work and best regards
Olaf

Target Market(s)

Young people with an affinity for social media and the web. Focus is on the female clientele.

Industry/Entity Type

Cosmetics

Font styles to use
Script

Colors
eea4c8
f59195
85cae6
cadf82

Requirements
Must have
• The logo must be included in some form. (PNG-File attached)
Nice to have
• Other types of packaging (can shape, packaging material)

```html
<!DOCTYPE html>
<html lang="en">
<head>
<meta charset="utf-8">
<title>say so cosmetics – jar labels</title>
<link rel="stylesheet" href="https://fonts.googleapis.com/css2?family=Pinyon+Script&display=swap">
<style>
  :root {
    --page: #ffffff;
    --label: #ffffff;
    --ink: #2b2b2b;
    --green: #c6df7f;
    --blue: #a9cdf2;
    --pink: #f3bfdf;
    --green-pattern-a: #bcd86a;
    --green-pattern-b: #6cc4cf;
    --green-pattern-c: #f2a15a;
    --blue-pattern-a: #9fc4ee;
    --blue-pattern-b: #9fe0d4;
    --blue-pattern-c: #c9df86;
    --pink-pattern-a: #ef9fcf;
    --pink-pattern-b: #a9cf5a;
    --pink-pattern-c: #8a8a80;
  }
  * { box-sizing: border-box; margin: 0; padding: 0; }
  html, body {
    width: 1200px;
    height: 665px;
    overflow: hidden;
    background: var(--page);
  }
  .canvas {
    position: relative;
    width: 1200px;
    height: 665px;
  }
  .label {
    position: absolute;
    top: 302px;
    width: 276px;
    height: 138px;
    background: var(--label);
    box-shadow: 0 0 0 1px #f0f0f0;
    overflow: hidden;
  }
  .label--green { left: 137px; }
  .label--blue  { left: 461px; }
  .label--pink  { left: 782px; }
  .pattern-band {
    position: absolute;
    left: 0;
    top: 0;
    width: 100%;
    height: 86px;
  }
  .label--green .pattern-band {
    background: linear-gradient(100deg, var(--green-pattern-c) 0%, var(--green-pattern-b) 25%, var(--green-pattern-a) 55%, var(--green-pattern-b) 80%, var(--green-pattern-a) 100%);
    opacity: .75;
  }
  .label--blue .pattern-band {
    background: linear-gradient(100deg, var(--blue-pattern-b) 0%, var(--blue-pattern-a) 30%, var(--blue-pattern-c) 60%, var(--blue-pattern-a) 100%);
    opacity: .7;
  }
  .label--pink .pattern-band {
    background: linear-gradient(100deg, var(--pink-pattern-a) 0%, var(--pink-pattern-b) 35%, var(--pink-pattern-a) 65%, var(--pink-pattern-c) 85%, var(--pink-pattern-a) 100%);
    opacity: .7;
  }
  .brand-dot {
    position: absolute;
    left: 18px;
    top: 40px;
    width: 84px;
    height: 84px;
    border-radius: 50%;
  }
  .label--green .brand-dot { background: var(--green); }
  .label--blue  .brand-dot { background: var(--blue); }
  .label--pink  .brand-dot { background: var(--pink); }
  .brand-name {
    position: absolute;
    left: 116px;
    top: 46px;
    width: 150px;
    font-family: "Pinyon Script", cursive;
    font-weight: 400;
    color: var(--ink);
    line-height: 1.1;
    white-space: nowrap;
  }
  .brand-name__main {
    display: block;
    font-size: 34px;
  }
  .brand-name__sub {
    display: block;
    font-size: 28px;
    padding-left: 14px;
  }
</style>
</head>
<body>
<main class="canvas">
  <section class="label label--green">
    <div class="pattern-band" role="img" aria-label="Abstract pattern of green spirals, teal leaf strokes, orange dots and grey marks"></div>
    <div class="brand-dot"></div>
    <p class="brand-name"><span class="brand-name__main">say so</span><span class="brand-name__sub">cosmetics</span></p>
  </section>

  <section class="label label--blue">
    <div class="pattern-band" role="img" aria-label="Abstract pattern of blue discs, mint strokes, green blobs and outlined leaves"></div>
    <div class="brand-dot"></div>
    <p class="brand-name"><span class="brand-name__main">say so</span><span class="brand-name__sub">cosmetics</span></p>
  </section>

  <section class="label label--pink">
    <div class="pattern-band" role="img" aria-label="Abstract pattern of pink organic shapes, green leaves and grey brush strokes"></div>
    <div class="brand-dot"></div>
    <p class="brand-name"><span class="brand-name__main">say so</span><span class="brand-name__sub">cosmetics</span></p>
  </section>
</main>
</body>
</html>
```